UK's largest boarding school requires an International travel brochure.

We are a large international boarding school in the UK (with 1400 boarders) and are looking for an International Travel brochure (16pp) which pulls together all of our international trips (India, Thailand, Costa Rica, USA, France, Venice, Iceland etc) together in order that parents may make an informed choice as to what they would like their child to do.
The brochure may include stock images as well as images of our students on the trip in previous years. I have attached a poster which was made in house for last year to give some idea, but we are open to a concept which conveys an educational image whilst getting you excited and inspired by the opportunities available. I have attached the 'blurb' collated to date but would need to be able to insert any missing information before sign-off.
Our school website is www.hollowmere.org and Facebook is https://www.facebook.com/HollowmereAbbotsCollege.
School logo attached. Link to some photos for use https://www.filevault-share.net/sc/m3rkd9wplq82zx7/BXK4TnPqRvMmYsHdLoJuXaW2c

Target Market(s)

Parents and students

Industry/Entity Type

School

Requirements
Must have
• Some images of previous trips.

```html
<!DOCTYPE html>
<html lang="en">
<head>
<meta charset="utf-8">
<title>International Trips 2015-16 Brochure</title>
<link rel="stylesheet" href="https://fonts.googleapis.com/css2?family=Cinzel:wght@400;700&family=Mulish:wght@400;700&display=swap">
<style>
  :root{
    --navy:#2b3372;
    --navy-deep:#1e2558;
    --gold:#e9ac2f;
    --white:#ffffff;
    --ink:#2a2a3a;
    --page-bg:#e6e6ea;
    --sky:#b9d6e6;
    --sea:#6fa7c4;
    --foliage:#4f7a3a;
    --stone:#5e6470;
  }
  *{box-sizing:border-box;margin:0;padding:0}
  html,body{width:1200px;height:1200px;overflow:hidden;background:var(--page-bg)}
  body{position:relative;font-family:"Mulish",sans-serif;color:var(--ink)}
  .spread{position:absolute;left:40px;width:1120px;height:540px;overflow:hidden;box-shadow:0 4px 14px rgba(0,0,0,.18)}
  .spread--cover{top:30px}
  .spread--inside{top:620px;background:var(--white)}
  .spread > svg{position:absolute;inset:0;width:100%;height:100%}
  .fold{position:absolute;top:0;bottom:0;left:559px;width:2px;background:rgba(0,0,0,.12)}

  /* cover */
  .crest{position:absolute;left:572px;top:258px;width:136px;height:136px;border-radius:50%;
    background:var(--white);border:6px solid var(--gold);display:flex;align-items:center;justify-content:center;text-align:center}
  .crest__name{font-family:"Cinzel",serif;font-weight:700;font-size:14px;line-height:1.25;color:var(--navy)}
  .cover-title{position:absolute;right:46px;top:440px;font-family:"Cinzel",serif;font-size:26px;color:var(--white);letter-spacing:1px}
  .contact{position:absolute;left:170px;top:330px;color:var(--white);font-size:14px;line-height:1.5}
  .contact li{list-style:none;display:flex;align-items:flex-start;gap:8px;margin-bottom:4px}
  .contact svg{width:14px;height:14px;flex:none;margin-top:3px}

  /* inside */
  .trip-left{position:absolute;left:30px;top:24px;width:510px}
  .trip-left h2{font-family:"Cinzel",serif;font-weight:700;font-size:31px;color:var(--navy);line-height:1}
  .trip-left h3{font-family:"Cinzel",serif;font-weight:700;font-size:19px;color:var(--gold);line-height:1.15}
  .trip-left .dates{font-family:"Cinzel",serif;font-weight:700;font-size:13.5px;color:var(--gold);margin-bottom:9px}
  .trip-left p{font-size:11px;line-height:1.3;margin-bottom:7px}
  .hl{color:var(--gold);font-weight:700}
  .trip-right{position:absolute;right:36px;top:166px;width:400px;text-align:right;color:var(--white)}
  .trip-right h2{font-family:"Cinzel",serif;font-size:34px;color:var(--gold);line-height:1}
  .trip-right h3{font-family:"Cinzel",serif;font-size:24px;color:var(--white);line-height:1.1}
  .trip-right .dates{font-family:"Cinzel",serif;font-weight:700;font-size:13px;margin-bottom:10px}
  .trip-right p{font-size:11px;line-height:1.3;margin-bottom:7px}
  .trip-right h4{font-family:"Cinzel",serif;font-size:19px;color:var(--gold);font-weight:400;margin:2px 0 4px}
  .syllabus{font-size:9.5px;line-height:1.45;color:#dfe2f2}
  .syllabus .dot{color:var(--gold)}
</style>
</head>
<body>

<section class="spread spread--cover" aria-label="Brochure cover spread">
  <svg viewBox="0 0 1120 540" preserveAspectRatio="none">
    <defs>
      <linearGradient id="navyGrad" x1="0" y1="0" x2="0" y2="1">
        <stop offset="0" stop-color="#323b80"/><stop offset="1" stop-color="#232a62"/>
      </linearGradient>
      <linearGradient id="lakeGrad" x1="0" y1="0" x2="0" y2="1">
        <stop offset="0" stop-color="#e9f3f8"/><stop offset=".45" stop-color="var(--sky)"/>
        <stop offset=".6" stop-color="var(--sea)"/><stop offset="1" stop-color="var(--stone)"/>
      </linearGradient>
      <linearGradient id="jungleGrad" x1="0" y1="0" x2="1" y2="1">
        <stop offset="0" stop-color="#6f9a4c"/><stop offset="1" stop-color="var(--foliage)"/>
      </linearGradient>
    </defs>
    <rect width="1120" height="540" fill="url(#navyGrad)"/>
    <rect x="0" y="250" width="560" height="290" fill="#3c4686" opacity=".35" role="img" aria-label="Faded group photo of students on a trip"/>
    <path d="M0,0 H520 C450,70 330,210 0,250 Z" fill="url(#jungleGrad)" role="img" aria-label="Photo of a student on a zip line in the forest"/>
    <path d="M0,250 C330,210 450,70 520,0" fill="none" stroke="var(--white)" stroke-width="4"/>
    <path d="M0,268 C345,226 465,80 545,0" fill="none" stroke="var(--gold)" stroke-width="14"/>
    <path d="M560,0 C470,110 470,300 620,360 C790,420 1000,330 1120,250 V0 Z" fill="url(#lakeGrad)" role="img" aria-label="Photo of a student sitting by a frozen lake with snowy mountains"/>
    <path d="M560,0 C470,110 470,300 620,360 C790,420 1000,330 1120,250" fill="none" stroke="var(--white)" stroke-width="4"/>
    <path d="M540,0 C448,115 450,315 615,378 C790,440 1010,350 1120,272" fill="none" stroke="var(--gold)" stroke-width="14"/>
  </svg>
  <div class="fold"></div>
  <div class="crest"><span class="crest__name">Hollowmere<br>Abbots<br>College</span></div>
  <h1 class="cover-title">International trips 2015-16</h1>
  <ul class="contact">
    <li><svg viewBox="0 0 14 14"><rect width="14" height="14" rx="3" fill="var(--gold)"/><path d="M4 3 L6 5 L5 6 Q6 8 8 9 L9 8 L11 10 L10 11 Q5 11 3 4 Z" fill="var(--navy)"/></svg>44 (0)1632 96 04 17</li>
    <li><svg viewBox="0 0 14 14"></svg>Hollowmere Abbots College, Hollowmere Estate,<br>Ashby Fell, North Yorkshire, HX9 4QT, UK</li>
    <li><svg viewBox="0 0 14 14"><rect x="1" y="3" width="12" height="8" fill="var(--gold)"/><path d="M1 3 L7 8 L13 3" fill="none" stroke="var(--navy)" stroke-width="1.2"/></svg>info@hollowmere.org</li>
    <li><svg viewBox="0 0 14 14"><circle cx="7" cy="7" r="6" fill="var(--gold)"/><path d="M1 7 H13 M7 1 V13" stroke="var(--navy)" stroke-width="1"/></svg>www.hollowmere.org</li>
  </ul>
</section>

<section class="spread spread--inside" aria-label="Brochure inside spread">
  <svg viewBox="0 0 1120 540" preserveAspectRatio="none">
    <defs>
      <linearGradient id="canalGrad" x1="0" y1="0" x2="0" y2="1">
        <stop offset="0" stop-color="#d9dde2"/><stop offset=".35" stop-color="#c6a690"/><stop offset=".7" stop-color="#5f8a86"/>
      </linearGradient>
      <linearGradient id="navyGrad2" x1="0" y1="0" x2="0" y2="1">
        <stop offset="0" stop-color="#323b80"/><stop offset="1" stop-color="#232a62"/>
      </linearGradient>
    </defs>
    <rect x="590" y="0" width="530" height="420" fill="url(#canalGrad)" role="img" aria-label="Photo of the Grand Canal in Venice with boats"/>
    <path d="M0,470 C300,500 520,450 600,380 C640,250 700,120 1120,80 V540 H0 Z" fill="url(#navyGrad2)"/>
    <path d="M0,470 C300,500 520,450 600,380 C640,250 700,120 1120,80" fill="none" stroke="var(--white)" stroke-width="4"/>
    <path d="M0,452 C300,482 510,432 586,364 C626,234 690,102 1120,62" fill="none" stroke="var(--gold)" stroke-width="12"/>
    <path d="M0,440 C300,470 502,420 576,353" fill="none" stroke="var(--white)" stroke-width="3"/>
  </svg>
  <div class="fold"></div>
  <div class="trip-left">
    <h2>October half term</h2>
    <h3>Netball tour to Lumière Parks, Paris</h3>
    <div class="dates">24th Oct to 28th Oct 2015 – open to girls in Years 6-10</div>
    <p>The trip is <span class="hl">open to girls</span> in years 6-10 (in the academic year 2015/16) and will depart from Hollowmere on Sunday 25th October and return on Thursday 29th October 2015.</p>
    <p>For young players this unique Festival provides them with the opportunity to take part in a professionally-organised overseas tournament, as well as enabling them to develop their netball skills, confidence and ability level through the support of expert coaches and England international and Superleague netball celebrities, at a highly enjoyable and fun destination.</p>
    <p>The coaching clinics and masterclasses are led by world-class players and coaches. These truly inspirational and passionate players and coaches, including England Internationals and Superleague players, are all involved in the game at the highest level.</p>
    <p>The girls will be staying at the Pinewood Frontier Lodge of <span class="hl">Lumière Parks Paris</span>, which offers a good standard of accommodation in a safe and secure environment. In addition, outside of the time devoted to netball, our included admission to both <span class="hl">Lumière Park and Lumière Studios Park</span> ensures that we are fully entertained throughout our time away.</p>
    <p>The cost of the trip is approx. £735 fully inclusive of all transport, travel insurance, cabin style accommodation, meals (breakfast, lunch and dinner), netball tournament, coaching clinics and Masterclass, entrance to the Lumière Parks, Match ball and Kit bag.</p>
  </div>
  <div class="trip-right">
    <h2>Dive trip</h2>
    <h3>to Gozo</h3>
    <div class="dates">24th Oct to 1st Nov 2015 – open to years 9-13</div>
    <p>The Islands of Gozo's clear blue Mediterranean sea is ideal for scuba diving and is accessible from the shore or boat in every part of the island. Offering excellent and unique diving experiences, creating an ultimate location for beginners and experienced divers alike, and with tiny Comino island, famous for its Blue Lagoon – form very special diving sites at the heart of the Mediterranean.</p>
    <p>The trip is <span class="hl">open to students in years 9-13</span> (in the academic year 2015/16) and will depart from Hollowmere on Sunday 25th October and return on Sunday 1st November 2015.</p>
    <h4>Scuba diving</h4>
    <div class="syllabus">
      Students will learn all the essential skills needed for scuba diving and the course is divided into the following –<br>
      Open water dives 1, 2, 3, 4. <span class="dot">●</span><br>
      Theory sections, Knowledge Review 1, 2, 3, 4. <span class="dot">●</span><br>
      Confined water training 1, 2, 3, 4, 5. <span class="dot">●</span> Online Registration as a certified diver with OWDA. <span class="dot">●</span>
    </div>
  </div>
</section>

</body>
</html>
```